Professional Services consultancy seeks modern, simple stationary

A new consultancy company based in Calgary, Canada, looking for an elegant, simple, modern stationary design. The Director has the artistic abilities of an inanimate object, and is seeking a corporate design package for letterhead, business cards, email sig blocks etc. We currently have nothing...

We have a pretty unique set of skills which make us stand out from the crowd...once we get in the door... We want to communicate reliability, professionalism but not too conservative, and ideally something that would highlight us in a crowded market. Above all though, we don't take ourselves too seriously (Australians...)

Target Market(s)

Our core services are based around occupational health, safety and industrial hygiene consulting, but looking at bringing other professional services under our banner - so not too specific.

Industry/Entity Type

Professional Service

Font styles to use
Sans Serif

Colors

Designer to choose colors to be used in the design.

Requirements
Must have
• We have a pretty unique set of skills which make us stand out from the crowd...once we get in the door... We want to communicate reliability, professionalism but not too conservative, and ideally something that would highlight us in a crowded market. Above all though, we don't take ourselves too seriously (Australians...)
Nice to have
• The company name, B & L Keystone Services Inc, is named for the Chinese zodiac signs of the Director's daughters, Rat and Tiger (they named it) - it would be nice if these characters could be incorporated into the design, but not essential. As for colours - I have a vibrant green in my mind but not sure why and open to any recommendations.

```html
<!DOCTYPE html>
<html lang="en">
<head>
<meta charset="utf-8">
<title>B &amp; L Keystone Services Inc — Business Card</title>
<link href="https://fonts.googleapis.com/css2?family=Lato:wght@400;700&display=swap" rel="stylesheet">
<style>
  :root {
    --navy: #1b3882;
    --ink: #4a4646;
    --paper: #ffffff;
    --edge: #6b6b6b;
  }
  html, body {
    margin: 0;
    padding: 0;
    width: 1199px;
    height: 1200px;
    overflow: hidden;
    background: var(--paper);
    font-family: "Lato", sans-serif;
  }
  .sheet {
    position: relative;
    width: 1199px;
    height: 1200px;
  }
  .card {
    position: absolute;
    left: 190px;
    width: 821px;
    height: 462px;
    border-radius: 41px;
    box-sizing: border-box;
    overflow: hidden;
  }
  .card--front {
    top: 121px;
    background: var(--navy);
  }
  .card--back {
    top: 617px;
    background: var(--paper);
    border: 1px solid var(--edge);
  }
  .brand-name {
    position: absolute;
    margin: 0;
    font-family: "Lato", sans-serif;
    font-weight: 700;
    font-size: 42px;
    line-height: 48px;
    letter-spacing: 0.5px;
  }
  .card--front .brand-name {
    left: 0;
    right: 0;
    top: 185px;
    text-align: center;
    color: var(--paper);
  }
  .card--back .brand-name {
    left: 57px;
    top: 70px;
    color: var(--navy);
  }
  .contact {
    position: absolute;
    left: 369px;
    top: 185px;
    color: var(--ink);
    font-size: 26.5px;
    line-height: 32px;
  }
  .contact p { margin: 0; white-space: nowrap; }
  .contact__name {
    font-weight: 700;
    font-size: 37px;
    line-height: 40px;
  }
  .contact__company {
    font-weight: 700;
    margin-top: 35px !important;
  }
</style>
</head>
<body>
  <div class="sheet">
    <section class="card card--front" aria-label="Card front">
      <p class="brand-name">B &amp; L Keystone<br>Services Inc</p>
    </section>

    <section class="card card--back" aria-label="Card back">
      <p class="brand-name">B &amp; L Keystone<br>Services Inc</p>
      <div class="contact">
        <p class="contact__name">Person Name</p>
        <p class="contact__phone">+01 000 222 33 44</p>
        <p class="contact__email">person.name@blkeystone.com</p>
        <p class="contact__company">B &amp; L Keystone Services Inc.</p>
        <p class="contact__address">Address will come here</p>
        <p class="contact__address">Address will come here</p>
      </div>
    </section>
  </div>
</body>
</html>
```